Accounting firm needing business card / letterhead designed
Marcus L. Tembrook, CPA
marcus@lumenfiledesk.com
www.lumenfiledesk.com
482 E Larkin Ave Larkfield, NV 89555
419-555-0172
Business

```html
<!DOCTYPE html>
<html lang="en">
<head>
<meta charset="utf-8">
<title>Lumen File Desk – Business Card</title>
<link rel="stylesheet" href="https://fonts.googleapis.com/css2?family=Open+Sans:wght@400;600;700&display=swap">
<style>
  :root {
    --bg: #2b2c2e;
    --deep-green: #062b28;
    --mid-green: #2f4a46;
    --mist: #f2f3f3;
    --grey-green: #8e9a98;
    --navy: #2e2a72;
    --white: #ffffff;
    --rule: #27403d;
    --icon: #1d2624;
  }
  * { box-sizing: border-box; margin: 0; padding: 0; }
  html, body { width: 1200px; height: 900px; overflow: hidden; background: var(--bg); }
  body { font-family: "Open Sans", sans-serif; position: relative; }

  .card {
    position: absolute;
    left: 250px;
    width: 700px;
    height: 400px;
    overflow: hidden;
    box-shadow: 0 8px 24px rgba(0,0,0,.45);
  }

  /* Front */
  .card--front {
    top: 40px;
    background: linear-gradient(180deg, var(--mist) 0%, #c9cfce 30%, var(--grey-green) 55%, var(--mid-green) 100%);
  }
  .card--front .banknotes {
    position: absolute; right: 0; top: 40px; width: 360px; height: 220px;
    background: linear-gradient(160deg, rgba(255,255,255,.35), rgba(160,170,165,.25));
  }
  .card--front .brand {
    position: absolute; left: 0; right: 0; top: 110px;
    text-align: center;
    color: var(--navy);
    font-weight: 700;
    font-size: 46px;
    letter-spacing: 6px;
  }
  .card--front .band {
    position: absolute; left: 0; right: 0; bottom: 0; height: 130px;
    background: var(--deep-green);
    display: flex; align-items: center; justify-content: center;
  }
  .card--front .website {
    color: var(--white); font-weight: 600; font-size: 24px; letter-spacing: 6px;
  }

  /* Back */
  .card--back {
    top: 470px;
    background: linear-gradient(180deg, #e9ecec 0%, var(--grey-green) 45%, var(--mid-green) 80%, #173633 100%);
  }
  .card--back .shapes { position: absolute; inset: 0; }
  .card--back .banknotes {
    position: absolute; left: 180px; top: 60px; width: 100px; height: 230px;
    background: linear-gradient(170deg, rgba(255,255,255,.4), rgba(190,198,195,.2));
  }
  .card--back .brand {
    position: absolute; left: 205px; top: 52px;
    color: var(--navy); font-weight: 700; font-size: 28px; letter-spacing: 3px;
  }
  .holder { position: absolute; left: 400px; top: 130px; width: 270px; text-align: center; }
  .holder__name { color: var(--white); font-weight: 600; font-size: 21px; letter-spacing: 3px; white-space: nowrap; }
  .holder__title { color: var(--white); font-weight: 600; font-size: 17px; letter-spacing: 2px; margin-top: 2px; }
  .holder__rule { height: 1px; background: var(--rule); margin: 12px 0 0; }

  .contacts { position: absolute; left: 300px; top: 225px; list-style: none; }
  .contacts li {
    display: flex; align-items: center; gap: 12px;
    color: var(--white); font-size: 14.5px; letter-spacing: 1.5px;
    margin-bottom: 16px;
    white-space: nowrap;
  }
  .contacts svg { width: 24px; height: 24px; flex: none; }
</style>
</head>
<body>

  <section class="card card--front" aria-label="Card front">
    <div class="banknotes" role="img" aria-label="Faint photo of stacked banknotes"></div>
    <div class="brand">LUMEN FILE DESK</div>
    <div class="band">
      <span class="website">www.lumenfiledesk.com</span>
    </div>
  </section>

  <section class="card card--back" aria-label="Card back">
    <svg class="shapes" viewBox="0 0 700 400" preserveAspectRatio="none" aria-hidden="true">
      <rect x="0" y="0" width="700" height="14" fill="#062b28"/>
      <path d="M0 14 H190 C150 120 150 260 240 400 H0 Z" fill="#062b28"/>
    </svg>
    <div class="banknotes" role="img" aria-label="Faint photo of stacked banknotes"></div>
    <div class="brand">LUMEN FILE DESK</div>

    <div class="holder">
      <div class="holder__name">Marcus L. Tembrook</div>
      <div class="holder__title">CPA</div>
      <div class="holder__rule"></div>
    </div>

    <ul class="contacts">
      <li>
        <svg viewBox="0 0 24 24" aria-hidden="true"><circle cx="12" cy="12" r="10.5" fill="none" stroke="#1d2624" stroke-width="1.5"/><rect x="6.5" y="8" width="11" height="8" fill="none" stroke="#1d2624" stroke-width="1.3"/><path d="M6.5 8 L12 12.5 L17.5 8" fill="none" stroke="#1d2624" stroke-width="1.3"/></svg>
        marcus@lumenfiledesk.com
      </li>
      <li>
        <svg viewBox="0 0 24 24" aria-hidden="true"><circle cx="12" cy="12" r="10.5" fill="none" stroke="#1d2624" stroke-width="1.5"/><path d="M12 18 C9 14 8 12.5 8 10.5 A4 4 0 0 1 16 10.5 C16 12.5 15 14 12 18 Z" fill="#1d2624"/><circle cx="12" cy="10.5" r="1.5" fill="#8e9a98"/></svg>
        482 E Larkin Ave Larkfield, NV 89555
      </li>
      <li>
        <svg viewBox="0 0 24 24" aria-hidden="true"><circle cx="12" cy="12" r="10.5" fill="none" stroke="#1d2624" stroke-width="1.5"/><path d="M9 6.5 L10.8 6.5 L11.5 9.5 L10.2 10.5 C10.8 12 11.8 13.2 13.3 13.9 L14.3 12.6 L17.2 13.3 L17.2 15.2 C17.2 16 16.5 16.7 15.6 16.6 C11.3 16.2 7.8 12.8 7.4 8.4 C7.3 7.4 8.1 6.5 9 6.5 Z" fill="#1d2624"/></svg>
        419-555-0172
      </li>
    </ul>
  </section>

</body>
</html>
```